Aged Care Consultancy Business needs a business card design

I need a two sided business card - I want it clean and professional. Surprise me

Target Market(s)

middle aged and ageing victorians

Industry/Entity Type

Health Care

Contact Information for Business Card

Text to be included

Logo
Aged Care Consulting Services
Professional, Reliable, Affordable

Tovan Brelsick
Director
0427 31 64 92 (larger)
1300 73 29 41
tovan@wadolire.com.au
www.wadolcare.com.au
Facebook (details TBA)

include little icons beside the contact info:

- Envelope = email
- Phone = phone
- Globe = website

Font styles to use
Serif
Sans Serif

Requirements
Must have
• look proffesional and clean

```html
<!DOCTYPE html>
<html lang="en">
<head>
<meta charset="utf-8">
<title>Wadol Care – Business Card</title>
<link rel="stylesheet" href="https://fonts.googleapis.com/css2?family=Roboto:wght@400;500;700&display=swap">
<style>
  :root {
    --bg: #e9e6e1;
    --white: #f7f7f5;
    --navy: #0a4a8f;
    --orange: #e8940a;
    --gold: #d9980f;
    --ink-light: #ffffff;
  }
  * { box-sizing: border-box; margin: 0; padding: 0; }
  html, body { width: 1200px; height: 1023px; overflow: hidden; }
  body {
    background: var(--bg);
    font-family: "Roboto", Arial, sans-serif;
    position: relative;
  }
  .card {
    position: absolute;
    left: 250px;
    width: 700px;
    height: 400px;
    border-radius: 18px;
    overflow: hidden;
    box-shadow: 0 6px 18px rgba(0,0,0,0.18);
  }
  .card--front { top: 80px; background: var(--white); }
  .card--back { top: 543px; background: var(--orange); }

  .front__logo-zone {
    position: absolute; left: 0; top: 0; width: 100%; height: 160px;
    display: flex; flex-direction: column; align-items: center; justify-content: center; gap: 6px;
  }
  .brand {
    display: flex; align-items: center; gap: 14px;
  }
  .brand-name {
    font-weight: 700;
    font-size: 52px;
    letter-spacing: -1px;
    color: var(--navy);
    line-height: 1;
  }
  .brand-dot {
    width: 34px; height: 34px; border-radius: 50%;
    background: var(--navy);
  }
  .service-line {
    font-size: 15px; font-weight: 500; color: var(--navy);
    letter-spacing: 0.5px; line-height: 1.2;
  }
  .tagline {
    font-size: 13px; font-weight: 400; color: var(--orange);
    letter-spacing: 0.5px; line-height: 1.2;
  }
  .front__band {
    position: absolute; left: 0; top: 160px; width: 100%; height: 200px;
    background: var(--navy);
  }
  .front__strip {
    position: absolute; left: 0; bottom: 0; width: 100%; height: 40px;
    background: var(--gold);
  }
  .identity {
    position: absolute; left: 60px; top: 92px;
    color: var(--ink-light);
  }
  .identity__name { font-size: 34px; font-weight: 500; line-height: 1.05; }
  .identity__role { font-size: 20px; color: var(--orange); text-align: right; }
  .band__divider {
    position: absolute; left: 392px; top: 20px; width: 1px; height: 160px;
    background: linear-gradient(to bottom, rgba(255,255,255,0), rgba(255,255,255,0.45), rgba(255,255,255,0));
  }
  .contacts {
    position: absolute; left: 420px; top: 28px;
    list-style: none; color: var(--ink-light);
    font-size: 16px; line-height: 1;
  }
  .contacts li { display: flex; align-items: center; gap: 12px; height: 34px; white-space: nowrap; }
  .contacts li.contacts__primary { font-size: 18px; font-weight: 500; }
  .contacts svg { width: 18px; height: 18px; flex: none; }

  .back__logo {
    position: absolute; inset: 0;
    display: flex; align-items: center; justify-content: center; gap: 20px;
  }
  .back__logo .brand-name { font-size: 72px; }
  .back__logo .brand-dot { width: 52px; height: 52px; }
</style>
</head>
<body>
  <section class="card card--front" aria-label="Business card front">
    <div class="front__logo-zone">
      <div class="brand">
        <span class="brand-dot"></span>
        <span class="brand-name">wadol care</span>
      </div>
      <p class="service-line">Aged Care Consulting Services</p>
      <p class="tagline">Professional, Reliable, Affordable</p>
    </div>
    <div class="front__band">
      <div class="identity">
        <p class="identity__name">Tovan Brelsick</p>
        <p class="identity__role">Director</p>
      </div>
      <div class="band__divider"></div>
      <ul class="contacts">
        <li class="contacts__primary">
          <svg viewBox="0 0 18 18"><circle cx="9" cy="9" r="8" fill="none" stroke="#e8940a" stroke-width="1.6"/><path d="M6 5.5c0 4 2.5 6.5 6.5 6.5l.5-1.6-2-.8-.8.9c-1-.5-2-1.5-2.5-2.5l.9-.8-.8-2z" fill="#e8940a"/></svg>
          0427 31 64 92
        </li>
        <li>
          <svg viewBox="0 0 18 18"><rect x="2" y="3" width="14" height="12" fill="none" stroke="#e8940a" stroke-width="1.6"/></svg>
          1300 73 29 41
        </li>
        <li>
          <svg viewBox="0 0 18 18"><rect x="1.5" y="4" width="15" height="10" fill="none" stroke="#e8940a" stroke-width="1.4"/><path d="M1.5 4l7.5 6 7.5-6M1.5 14l5.5-5M16.5 14l-5.5-5" fill="none" stroke="#e8940a" stroke-width="1.2"/></svg>
          tovan@wadolire.com.au
        </li>
        <li>
          <svg viewBox="0 0 18 18"><circle cx="9" cy="9" r="7.5" fill="none" stroke="#e8940a" stroke-width="1.4"/><ellipse cx="9" cy="9" rx="3.2" ry="7.5" fill="none" stroke="#e8940a" stroke-width="1.2"/><path d="M1.5 9h15M3 5h12M3 13h12" fill="none" stroke="#e8940a" stroke-width="1.1"/></svg>
          www.wadolcare.com.au
        </li>
      </ul>
    </div>
    <div class="front__strip"></div>
  </section>

  <section class="card card--back" aria-label="Business card back">
    <div class="back__logo">
      <span class="brand-dot"></span>
      <span class="brand-name">wadol care</span>
    </div>
  </section>
</body>
</html>
```